Contemporary Elegant Business Card Design for an International Trade Company in the Wine Industry

We need a new business card design for an international trade company in the wine and winemaking industry. The overall feel of the card should be contemporary, upscale, luxurious and elegant. It should communicate confidence and professionalism. The colors should complementary to our logo design (burgundy, gold, and black).
Inspiration: rich velvet tapestry
The card should include the following information:
Business: Brovenna Trading/Shipping, LLC.
Name: Marcus T. Hollenbrand
Title: CEO
Email: mark@brovennatrading.example
Phone: 555-294-6172
www.brovennatrading.example
Updates
Project Deadline Extended
Reason: We'd like the designers that we requested some additional designs from to still submit designs. Thank you!
Industry/Entity Type
Business
Contact Information for Business Card
Title: CEO
Phone: 555-294-6172
www.brovennatrading.example
Look and feel

```html
<!DOCTYPE html>
<html lang="en">
<head>
<meta charset="utf-8">
<title>Brovenna Trading/Shipping – Business Card</title>
<link rel="stylesheet" href="https://fonts.googleapis.com/css2?family=Marcellus&family=Marcellus+SC&family=Crimson+Text:wght@400;600&display=swap">
<style>
  :root {
    --backdrop: #d6d6d6;
    --paper: #eeebe8;
    --paper-light: #f5f3f0;
    --paper-shade: #dedad6;
    --paper-fleck: rgba(190, 184, 178, 0.35);
    --panel: #f9f8f6;
    --burgundy: #7d1a22;
    --ink: #1d1b1a;
    --gold: #e4cf92;
  }
  * { margin: 0; padding: 0; box-sizing: border-box; }
  html, body {
    width: 1200px;
    height: 926px;
    overflow: hidden;
    background: var(--backdrop);
  }
  .canvas {
    position: relative;
    width: 1200px;
    height: 926px;
  }
  .card {
    position: absolute;
    left: 280px;
    width: 640px;
    height: 366px;
    background:
      radial-gradient(ellipse 180px 90px at 18% 22%, var(--paper-light), transparent 70%),
      radial-gradient(ellipse 220px 120px at 72% 30%, var(--paper-fleck), transparent 70%),
      radial-gradient(ellipse 160px 110px at 35% 78%, var(--paper-fleck), transparent 70%),
      radial-gradient(ellipse 200px 100px at 85% 80%, var(--paper-light), transparent 70%),
      radial-gradient(ellipse 140px 80px at 55% 55%, rgba(255,255,255,0.45), transparent 70%),
      linear-gradient(125deg, var(--paper) 0%, var(--paper-shade) 45%, var(--paper) 70%, var(--paper-shade) 100%);
    box-shadow: 0 1px 0 #fff inset, 0 8px 22px rgba(0,0,0,0.22), 0 2px 4px rgba(0,0,0,0.12);
  }
  .card--back { top: 60px; }
  .card--front { top: 496px; }

  .brand-panel {
    position: absolute;
    background: var(--panel);
    display: flex;
    flex-direction: column;
    align-items: center;
    justify-content: center;
    gap: 12px;
    box-shadow: 0 0 0 1px rgba(0,0,0,0.03);
  }
  .brand-mark {
    width: 22px;
    height: 22px;
    background: var(--burgundy);
    flex: none;
  }
  .brand-name {
    font-family: "Marcellus", serif;
    color: var(--burgundy);
    font-size: 30px;
    letter-spacing: 1px;
  }

  .card--back .brand-panel {
    left: 230px;
    top: 40px;
    width: 180px;
    height: 180px;
  }
  .company-name {
    position: absolute;
    left: 0;
    right: 0;
    top: 250px;
    text-align: center;
    font-family: "Marcellus SC", serif;
    font-size: 21px;
    letter-spacing: 1.5px;
    color: var(--ink);
  }

  .card--front .brand-panel {
    left: 56px;
    top: 18px;
    width: 170px;
    height: 170px;
  }
  .person {
    position: absolute;
    left: 44px;
    top: 206px;
    display: inline-block;
  }
  .person-name {
    font-family: "Marcellus SC", serif;
    font-size: 17px;
    letter-spacing: 1px;
    color: var(--burgundy);
    white-space: nowrap;
  }
  .person-title {
    font-family: "Marcellus SC", serif;
    font-size: 11px;
    color: var(--burgundy);
    text-align: right;
    margin-top: 3px;
  }
  .contact {
    position: absolute;
    left: 44px;
    top: 244px;
    list-style: none;
    font-family: "Crimson Text", serif;
    font-size: 17px;
    line-height: 21px;
    color: var(--ink);
  }
  .contact-phone { font-size: 18px; }
  .accent-bar {
    position: absolute;
    left: 44px;
    bottom: 36px;
    width: 200px;
    height: 8px;
    background: var(--gold);
  }
</style>
</head>
<body>
  <main class="canvas">
    <section class="card card--back" aria-label="Business card, back">
      <div class="brand-panel">
        <span class="brand-mark"></span>
        <span class="brand-name">Brovenna</span>
      </div>
      <p class="company-name">Brovenna Trading/Shipping, LLC.</p>
    </section>

    <section class="card card--front" aria-label="Business card, front">
      <div class="brand-panel">
        <span class="brand-mark"></span>
        <span class="brand-name">Brovenna</span>
      </div>
      <div class="person">
        <p class="person-name">Marcus T. Hollenbrand</p>
        <p class="person-title">CEO</p>
      </div>
      <ul class="contact">
        <li class="contact-phone">555-294-6172</li>
        <li>brovennatrading.example</li>
        <li>mark@brovennatrading.example</li>
      </ul>
      <div class="accent-bar"></div>
    </section>
  </main>
</body>
</html>
```